Business card, Stationery and form for Crane Mill
Crane Mill, LLC an Energy Broker
Professional
Desmond Pilkerton
Principal
47 Birchway Lane
Lakewood, NJ 08539
(555) 214-KELP (5357)
dpilkerton@cranemill.com
www.cranemill.com
I will need to be able to change names etc on them for other workers.
Attached you will find a form that we use regularly (see the comment for the file).
I would also need the stationary designed in a way that is easy to use for word processing in MS Word, such as a template or in a word document that I can type on, besides in any way that may be printed.
I am guessing to use the secondary logo for the back but this is not required. An idea that I had but am unsure how it would look is to make that logo larger and then to place the words inside the lower grey area.
I may choose a full color design with pictures besides the more traditional one which I prefer in order to give the sales force a choice.
This is our primary logo
This is our secondary logo
This is a form which we use regularly. We primarily use the excel version here: http://cranemill.com/wp-content/uploads/2012/03/Crane-Mill-LOA-Form-unprotected.xlsx The form gets minor edits from time to time and I would prefer to have it designed as a header and footer or a template.

```html
<!DOCTYPE html>
<html lang="en">
<head>
<meta charset="utf-8">
<title>Crane Mill Stationery</title>
<link href="https://fonts.googleapis.com/css2?family=Open+Sans:wght@400;600;700&display=swap" rel="stylesheet">
<style>
  :root{
    --board-top:#2f868d;
    --board-mid:#1f6d76;
    --board-deep:#134d56;
    --brand-blue:#0f5fa6;
    --brand-teal:#1fa6c6;
    --brand-navy:#0b2f5c;
    --paper:#ffffff;
    --ink:#33465a;
    --muted:#9fc3c8;
    --label:#cfe6e8;
    --envelope-dark:#141a1f;
  }
  *{box-sizing:border-box;margin:0;padding:0}
  html,body{width:1200px;height:382px;overflow:hidden}
  body{font-family:"Open Sans",Arial,sans-serif;
    background:linear-gradient(180deg,var(--board-top) 0%,var(--board-mid) 55%,var(--board-deep) 100%);
    position:relative;color:var(--ink)}
  .item{position:absolute}
  .label{position:absolute;font-size:5px;color:var(--label);text-align:center;width:100%;bottom:-9px}
  .wordmark{display:flex;align-items:center;gap:4px;font-weight:700;color:var(--brand-blue);letter-spacing:.3px;white-space:nowrap}
  .wordmark .dot{border-radius:50%;background:var(--brand-teal);flex:none}

  /* brand intro */
  .intro{left:28px;top:38px;width:190px}
  .intro .wordmark{font-size:17px}
  .intro .wordmark .dot{width:16px;height:16px}
  .tagline{font-size:5.5px;color:#e6f3f4;letter-spacing:.6px;margin:5px 0 0 22px}
  .concepts{font-size:5px;color:var(--label);margin:10px 0 0 48px}

  /* business cards */
  .card{position:absolute;width:148px;height:86px;background:var(--paper);overflow:hidden}
  .card-front-a{left:12px;top:150px;overflow:visible}
  .card-back-a{left:172px;top:150px}
  .card-front-b{left:12px;top:262px;overflow:visible;background:linear-gradient(135deg,var(--brand-blue),var(--brand-navy))}
  .card-back-b{left:172px;top:262px}
  .card .centered{position:absolute;inset:0;display:flex;align-items:center;justify-content:center}
  .card .wordmark{font-size:11px}
  .card .wordmark .dot{width:11px;height:11px}
  .card-front-b .wordmark{color:#fff}
  .card svg.swoosh{position:absolute;left:0;top:0}
  .contact{position:absolute;right:8px;top:12px;text-align:right;font-size:4.6px;line-height:1.45;color:var(--ink)}
  .contact .person{font-weight:700;font-size:6px;color:var(--brand-blue)}
  .contact .role{font-size:4.8px;margin-bottom:3px}

  /* letterheads */
  .letterhead{position:absolute;top:18px;width:184px;height:344px;background:var(--paper);overflow:hidden}
  .letterhead-a{left:392px}
  .letterhead-b{left:600px}
  .letterhead .wordmark{position:absolute;left:14px;top:14px;font-size:8px}
  .letterhead .wordmark .dot{width:9px;height:9px}
  .letterhead .head-info{position:absolute;right:12px;top:15px;font-size:3.6px;line-height:1.5;text-align:right;color:var(--ink)}
  .watermark{position:absolute;left:30px;top:95px;width:124px;height:150px;border-radius:50%;
    background:radial-gradient(ellipse at center,rgba(31,166,198,.18) 0%,rgba(31,166,198,.06) 55%,rgba(255,255,255,0) 75%)}
  .letterhead svg{position:absolute;left:0}
  .sheet-label{position:absolute;top:366px;font-size:5px;color:var(--label);width:184px;text-align:center}

  /* envelopes */
  .envelope{position:absolute;width:308px;background:var(--paper);overflow:hidden;box-shadow:0 1px 3px rgba(0,0,0,.25)}
  .envelope-dark{left:878px;top:18px;height:92px}
  .envelope-light{left:878px;top:116px;height:78px}
  .envelope-plain{left:878px;top:170px;height:94px}
  .envelope svg{position:absolute;left:0;top:0}
  .envelope .wordmark{position:absolute;font-size:8px}
  .envelope .wordmark .dot{width:8px;height:8px}
  .envelope-dark .wordmark{left:50%;top:22px;transform:translateX(-50%);color:#fff}
  .envelope-light .wordmark{left:50%;top:18px;transform:translateX(-50%)}
  .small-envelope{position:absolute;left:864px;top:224px;width:132px;height:62px;background:var(--paper);overflow:hidden;
    box-shadow:0 1px 3px rgba(0,0,0,.3)}
  .small-envelope .wordmark{position:absolute;left:8px;top:9px;font-size:6px}
  .small-envelope .wordmark .dot{width:6px;height:6px}
  .small-envelope svg{position:absolute;left:0;bottom:0}
  .env-label{position:absolute;left:878px;top:292px;width:132px;text-align:center;font-size:5px;color:var(--label)}
</style>
</head>
<body>

  <section class="item intro">
    <div class="wordmark"><span class="dot"></span>Crane Mill</div>
    <p class="tagline">SMART ENERGY BUYING FOR YOUR BUSINESS</p>
    <p class="concepts">Reference Concepts</p>
  </section>

  <!-- business cards -->
  <div class="card card-front-a">
    <div class="centered"><div class="wordmark"><span class="dot"></span>Crane Mill</div></div>
    <span class="label">Business Card 1</span>
  </div>

  <div class="card card-back-a">
    <svg class="swoosh" width="148" height="86" viewBox="0 0 148 86">
      <path d="M0 0 H40 C22 30 26 60 52 86 H0 Z" fill="var(--brand-blue)"/>
      <path d="M40 0 C22 30 26 60 52 86" fill="none" stroke="var(--brand-teal)" stroke-width="2"/>
    </svg>
    <div class="contact">
      <div class="person">Desmond Pilkerton</div>
      <div class="role">Principal</div>
      47 Birchway Lane<br>Lakewood, NJ 08539<br>(555) 214-KELP (5357)<br>dpilkerton@cranemill.com<br>www.cranemill.com
    </div>
  </div>

  <div class="card card-front-b">
    <div class="centered"><div class="wordmark"><span class="dot"></span>Crane Mill</div></div>
    <span class="label">Business Card 3</span>
  </div>

  <div class="card card-back-b">
    <svg class="swoosh" width="148" height="86" viewBox="0 0 148 86">
      <path d="M0 60 C40 50 90 70 148 56 V86 H0 Z" fill="var(--brand-blue)"/>
      <path d="M0 56 C40 46 90 66 148 52" fill="none" stroke="var(--brand-teal)" stroke-width="2"/>
    </svg>
    <div class="contact" style="top:8px">
      <div class="person">Desmond Pilkerton</div>
      <div class="role">Principal</div>
      47 Birchway Lane, Lakewood, NJ 08539<br>(555) 214-KELP (5357)<br>dpilkerton@cranemill.com
    </div>
  </div>

  <!-- letterheads -->
  <div class="letterhead letterhead-a">
    <div class="wordmark"><span class="dot"></span>Crane Mill</div>
    <div class="head-info">47 Birchway Lane<br>Lakewood, NJ 08539<br>www.cranemill.com</div>
    <svg width="184" height="20" viewBox="0 0 184 20" style="top:36px">
      <path d="M0 10 C60 2 120 18 184 6" fill="none" stroke="var(--brand-teal)" stroke-width="1"/>
    </svg>
    <div class="watermark" role="img" aria-label="Faint brand watermark"></div>
    <svg width="184" height="30" viewBox="0 0 184 30" style="bottom:0">
      <path d="M0 14 C60 4 120 22 184 8 V30 H0 Z" fill="var(--brand-blue)"/>
      <path d="M0 10 C60 0 120 18 184 4" fill="none" stroke="var(--brand-teal)" stroke-width="1.5"/>
    </svg>
  </div>
  <p class="sheet-label" style="left:392px">Letterhead Design A</p>

  <div class="letterhead letterhead-b">
    <div class="wordmark"><span class="dot"></span>Crane Mill</div>
    <div class="head-info">(555) 214-KELP (5357)<br>dpilkerton@cranemill.com<br>www.cranemill.com</div>
    <div class="watermark" role="img" aria-label="Faint brand watermark"></div>
    <svg width="184" height="40" viewBox="0 0 184 40" style="bottom:0">
      <path d="M0 22 C70 8 120 30 184 14 V40 H0 Z" fill="var(--brand-navy)"/>
      <path d="M0 18 C70 4 120 26 184 10" fill="none" stroke="var(--brand-teal)" stroke-width="2"/>
    </svg>
  </div>
  <p class="sheet-label" style="left:600px">Letterhead Design B</p>

  <!-- envelopes -->
  <div class="envelope envelope-dark">
    <svg width="308" height="92" viewBox="0 0 308 92">
      <path d="M0 0 H308 V46 C208 64 100 64 0 46 Z" fill="var(--envelope-dark)"/>
      <path d="M0 46 C100 64 208 64 308 46" fill="none" stroke="var(--brand-teal)" stroke-width="2"/>
    </svg>
    <div class="wordmark"><span class="dot"></span>Crane Mill</div>
  </div>

  <div class="envelope envelope-light">
    <svg width="308" height="78" viewBox="0 0 308 78">
      <path d="M0 0 H308 V6 L154 48 L0 6 Z" fill="var(--brand-teal)" opacity=".35"/>
      <path d="M0 0 L154 44 L308 0" fill="none" stroke="var(--brand-teal)" stroke-width="1.5"/>
    </svg>
    <div class="wordmark"><span class="dot"></span>Crane Mill</div>
  </div>

  <div class="envelope envelope-plain">
    <svg width="308" height="94" viewBox="0 0 308 94">
      <path d="M0 0 L154 40 L308 0" fill="none" stroke="var(--muted)" stroke-width="1"/>
    </svg>
  </div>

  <div class="small-envelope">
    <div class="wordmark"><span class="dot"></span>Crane Mill</div>
    <svg width="132" height="18" viewBox="0 0 132 18">
      <path d="M0 8 C44 2 88 14 132 4 V18 H0 Z" fill="var(--brand-blue)"/>
    </svg>
  </div>
  <p class="env-label">Envelope Design Set</p>

</body>
</html>
```